Paths to Delight E-card design - Potential for other work

I am looking for a designer to create e card, thank you design templates for my new not for profit website www.pathstodelight.com.au.

They will have simple imagery, with a subtle and soft illustration which reflects some sort of emotion. Think of patterns and textures.

The main focus of the card will be the text submitted as the "Path to Delight". For an example of the text please see http://www.pathstodelight.com.au/search-for-ideas/.

The width of the card / image (which will be displayed on a web page) will be 700px max, and there is no restriction on height.

The colours will be similar to the website colours although possibly softer/pastal colours.

The design should contain a header/title "You've amazed me, thank you" before the actual words merged from the site as the Path to Delight. It will appear on a blank page on the website with the same header so it doesn't have to be similar to the website design.

I will upload similar designs I like to make your job easier on Monday.

Although this job is only for a couple of simple designs, I will require more in the future so there is potential for ongoing work. I am therefore looking for a provider who is reliable, trustworthy, efficient and of course has a creative design flair.

If you want to be a part of a great cause, please submit your designs. I look forward to working with you.

Thank you.

Target Market(s)

Everyone with a kind heart ;0)

Industry/Entity Type

Work

Requirements
Nice to have
• In terms of the attached files, 1 and 2 give an example of a pattern that is quite nice. Number 4 shows the colours I quite like with the orange. We want the e card to evoke emotion. (please note the design Is for an e card, not business card. This is just an example of a design, please ignore the fact it is on a business card.
Should not have
• Too much going on

```html
<!DOCTYPE html>
<html lang="en">
<head>
<meta charset="utf-8">
<title>Paths to Delight – Thank You E-card</title>
<link rel="stylesheet" href="https://fonts.googleapis.com/css2?family=Cormorant+Garamond:ital,wght@1,600&family=Questrial&display=swap">
<style>
  :root {
    --page-bg: #1c1c1c;
    --orange-deep: #e8561f;
    --orange-mid: #f27524;
    --orange-bright: #f7931e;
    --orange-soft: rgba(255, 214, 170, 0.30);
    --orange-soft-fade: rgba(255, 214, 170, 0);
    --cream: #fff3e0;
    --white: #ffffff;
    --title-shadow: rgba(90, 30, 0, 0.55);
  }
  * { margin: 0; padding: 0; box-sizing: border-box; }
  html, body {
    width: 1200px;
    height: 900px;
    overflow: hidden;
    background: var(--page-bg);
  }
  .stage {
    width: 1200px;
    height: 900px;
    display: flex;
    align-items: center;
    justify-content: center;
  }
  .ecard {
    position: relative;
    width: 1000px;
    height: 580px;
    overflow: hidden;
    background: radial-gradient(ellipse at 48% 55%, var(--orange-bright) 0%, var(--orange-mid) 45%, var(--orange-deep) 100%);
  }
  .ecard__decoration {
    position: absolute;
    left: 0;
    top: 250px;
    width: 1000px;
    height: 330px;
    background: linear-gradient(160deg, var(--orange-soft-fade) 0%, var(--orange-soft) 50%, var(--orange-soft-fade) 100%);
  }
  .ecard__title {
    position: absolute;
    left: 0;
    right: 0;
    top: 175px;
    text-align: center;
    font-family: "Cormorant Garamond", Georgia, serif;
    font-style: italic;
    font-weight: 600;
    font-size: 76px;
    line-height: 1;
    letter-spacing: 1px;
    color: var(--white);
    text-shadow: 2px 2px 2px var(--title-shadow);
    white-space: nowrap;
  }
  .ecard__url {
    position: absolute;
    right: 70px;
    bottom: 70px;
    font-family: "Questrial", "Century Gothic", sans-serif;
    font-size: 28px;
    letter-spacing: 1px;
    color: var(--cream);
  }
</style>
</head>
<body>
<main class="stage">
  <section class="ecard" aria-label="Thank you e-card">
    <div class="ecard__decoration" role="img" aria-label="Soft flowing light wave lines sweeping across the card from lower left to upper right"></div>
    <h1 class="ecard__title">You've amazed me, thank you</h1>
    <p class="ecard__url">www.pathstodelight.com.au</p>
  </section>
</main>
</body>
</html>
```